SLA & Internet Advert

Advertise some of our key SLA services & Internet Connectivity services.
Service Level Agreement:
Unlimited Remote, Email, Helpdesk & Telephone Support.
Unlimited Service Calls
Support Hours Monday - Saturday 7am-10pm Sunday till 5pm
Free additional visits during quorlam periods
Free remote access to school server for staff members
Free mobile device management for tablet devices
Free Email&Webhosting Service
Remote support on every device in school allowing us to close 90% of tickets within 30 mins.
Service Level Agreement Package 1 - Includes all the above + 1 Site visit every 2 weeks £2,500 per annum
Service Level Agreement Package 2 - Includes all the above + 1 Site Visit every week £4,500 per annum
Service Level Agreement Package 3 - Includes all the above + 2 Site visits every week - £7,540 per annum
Internet Connectivity (medium/large Primary)
Managed Firewall
Managed Web filter & Safeguarding
User reporting portal/email reporting.
Main Internet Line 1000 mb/s download 100mb/s upload
Back up Internet Line 80mb/s download 20mb/s upload
100% uptime guaranteed.
£3000 per annum
Internet Connectivity (Small Primary School)
Managed Firewall
£2100 per annum
My website is https://www.varnoquell.co.uk if you need any further information like phone numbers / email address etc
Education

```html
<!DOCTYPE html>
<html lang="en">
<head>
<meta charset="utf-8">
<title>SLA &amp; Internet Connectivity Services</title>
<link href="https://fonts.googleapis.com/css2?family=Montserrat:wght@400;500&family=Roboto:wght@400;500;700&family=Roboto+Condensed:wght@700&display=swap" rel="stylesheet">
<style>
  :root {
    --blue: #1f4b9c;
    --blue-dark: #1a3f86;
    --orange: #f07f45;
    --orange-deep: #e0673a;
    --ink: #1c1c1c;
    --paper: #ffffff;
    --tick: #22c08a;
  }
  * { box-sizing: border-box; margin: 0; padding: 0; }
  html, body { width: 800px; height: 1200px; overflow: hidden; background: #f4f4f4; }
  body { font-family: "Roboto", Arial, sans-serif; color: var(--ink); }
  .flyer { position: relative; width: 800px; height: 1200px; background: var(--paper); overflow: hidden; }

  .hero { position: absolute; left: 0; top: 0; width: 800px; height: 398px; background: var(--blue); color: #fff; }
  .hero-title { position: absolute; left: 40px; top: 48px; font-family: "Montserrat", Arial, sans-serif; font-weight: 400; font-size: 37px; line-height: 46px; }
  .hero-rule { position: absolute; left: 40px; top: 250px; width: 42px; height: 4px; background: #fff; }
  .hero-subtitle { position: absolute; left: 40px; top: 288px; font-family: "Montserrat", Arial, sans-serif; font-size: 21px; }
  .hero-lede { position: absolute; left: 40px; top: 325px; width: 300px; font-size: 12.5px; line-height: 17px; }
  .hero-art { position: absolute; left: 360px; top: 30px; width: 425px; height: 356px; border-radius: 6px;
    background: radial-gradient(circle at 50% 60%, #3a63b8 0%, #2a56aa 45%, var(--blue) 80%); }

  .hours-band { position: absolute; left: 0; top: 398px; width: 800px; height: 44px; background: var(--orange);
    font-weight: 500; font-size: 14.5px; line-height: 44px; padding-left: 40px; color: var(--ink); }

  .perk { position: absolute; display: flex; align-items: center; gap: 0; font-size: 11.5px; line-height: 14px; }
  .perk svg { flex: none; }
  .perk-text { position: absolute; left: 57px; width: 120px; }

  .promise { position: absolute; left: 470px; top: 478px; width: 300px; }
  .promise-line { font-size: 16px; line-height: 19px; padding-left: 47px; }
  .promise-stat { font-size: 17px; margin-top: 14px; }

  .sla-heading { position: absolute; left: 470px; top: 576px; font-weight: 700; font-size: 22px; }

  .package { position: absolute; left: 470px; width: 282px; height: 158px; background: var(--orange);
    border-radius: 18px 36px 36px 18px; overflow: hidden; }
  .package-tab { position: absolute; left: 0; top: 0; width: 40px; height: 100%; background: var(--blue); border-radius: 18px 0 0 18px; }
  .package-tab span { position: absolute; left: 50%; top: 50%; transform: translate(-50%, -50%) rotate(-90deg);
    white-space: nowrap; color: #fff; font-weight: 500; font-size: 17px; }
  .package-note { position: absolute; left: 58px; top: 22px; width: 200px; font-size: 13px; line-height: 17px; }
  .package-price { position: absolute; left: 57px; bottom: 20px; display: flex; align-items: flex-end; gap: 14px; color: #fff; }
  .price-figure { font-family: "Roboto Condensed", Arial Narrow, sans-serif; font-weight: 700; font-size: 46px; line-height: 46px; }
  .price-term { font-size: 21px; line-height: 23px; }

  .net-heading { position: absolute; left: 40px; color: var(--blue); font-weight: 700; font-size: 15px; }
  .net-item { position: absolute; font-size: 11.5px; line-height: 15px; width: 180px; }
  .net-item::before { content: ""; position: absolute; left: -19px; top: 4px; border-left: 5px solid var(--ink);
    border-top: 3.5px solid transparent; border-bottom: 3.5px solid transparent; }

  .footer { position: absolute; left: 0; top: 1133px; width: 800px; height: 67px; }
  .footer-blue { position: absolute; left: 260px; top: 0; width: 540px; height: 67px; background: var(--blue); border-top-right-radius: 26px; }
  .footer-phone { position: absolute; left: 0; top: 0; width: 302px; height: 67px; background: var(--orange-deep); border-top-right-radius: 26px;
    display: flex; align-items: center; padding-left: 42px; gap: 18px; color: #fff; font-size: 28px; }
  .footer-link { position: absolute; top: 0; height: 67px; display: flex; align-items: center; gap: 8px; color: #fff; font-size: 11.5px; }
  .footer-brand { position: absolute; left: 598px; top: 0; height: 67px; display: flex; align-items: center; gap: 7px;
    color: #fff; font-weight: 700; font-size: 18px; letter-spacing: 0.5px; }
  .brand-square { width: 12px; height: 12px; background: #fff; }
</style>
</head>
<body>
<main class="flyer">

  <header class="hero">
    <h1 class="hero-title">SLA services<br>&amp; Internet<br>Connectivity<br>services</h1>
    <div class="hero-rule"></div>
    <h2 class="hero-subtitle">Service Level Agreement:</h2>
    <p class="hero-lede">Unlimited Remote, Email, Helpdesk &amp; Telephone Support. Unlimited Service Calls</p>
    <div class="hero-art" role="img" aria-label="Illustration of IT support staff helping users around a large laptop screen with a help speech bubble, gears and clouds"></div>
  </header>

  <div class="hours-band">SUPPORT HOURS MONDAY - SATURDAY 7AM-10PM SUNDAY TILL 5PM</div>

  <div class="perk" style="left:40px; top:482px; height:48px;">
    <svg width="32" height="46" viewBox="0 0 32 46" fill="none" stroke="#1f4b9c" stroke-width="2">
      <path d="M16 44 C16 44 3 26 3 16 A13 13 0 0 1 29 16 C29 26 16 44 16 44 Z"/>
      <circle cx="16" cy="16" r="7"/>
      <path d="M11 40 Q16 46 21 40"/>
    </svg>
    <span class="perk-text">Free additional visits during quorlam periods</span>
  </div>
  <div class="perk" style="left:258px; top:482px; height:48px;">
    <svg width="20" height="46" viewBox="0 0 20 46" fill="none" stroke="#1f4b9c" stroke-width="2">
      <rect x="3" y="8" width="14" height="34" rx="3"/>
      <line x1="7" y1="2" x2="13" y2="2"/>
      <circle cx="10" cy="17" r="2"/><line x1="7" y1="25" x2="13" y2="25"/><line x1="7" y1="31" x2="13" y2="31"/>
    </svg>
    <span class="perk-text" style="left:42px; width:140px;">Free remote access to school server for staff members</span>
  </div>
  <div class="perk" style="left:40px; top:588px; height:46px;">
    <svg width="34" height="42" viewBox="0 0 34 42" fill="none" stroke="#1f4b9c" stroke-width="2">
      <rect x="2" y="2" width="24" height="26"/>
      <line x1="6" y1="9" x2="22" y2="9"/><line x1="6" y1="15" x2="22" y2="15"/>
      <rect x="16" y="18" width="16" height="22"/><line x1="20" y1="25" x2="28" y2="25"/>
    </svg>
    <span class="perk-text">Free mobile device management for tablet devices</span>
  </div>
  <div class="perk" style="left:250px; top:588px; height:46px;">
    <svg width="36" height="26" viewBox="0 0 36 26" fill="none" stroke="#1f4b9c" stroke-width="2">
      <rect x="2" y="2" width="32" height="22"/><path d="M2 2 L18 15 L34 2"/>
    </svg>
    <span class="perk-text" style="left:50px; width:110px;">Free Email&amp;Web-hosting Service</span>
  </div>

  <div class="promise">
    <svg width="36" height="36" viewBox="0 0 36 36" style="position:absolute; left:0; top:-2px;">
      <path d="M18 1 L22 5 L28 4 L29 10 L34 14 L31 19 L33 25 L27 27 L25 33 L19 31 L14 35 L10 30 L4 29 L5 23 L1 18 L5 13 L4 7 L10 6 L13 1 Z" fill="#22c08a"/>
      <path d="M11 18 L16 23 L25 13" stroke="#fff" stroke-width="3" fill="none"/>
    </svg>
    <p class="promise-line">Remote support on every device in school allowing us to close</p>
    <p class="promise-stat">90% of tickets within 30 mins.</p>
  </div>

  <h3 class="sla-heading">Service Level Agreement</h3>

  <section class="package" style="top:619px;">
    <div class="package-tab"><span>Package 1</span></div>
    <p class="package-note">Includes all the above + 1 Site visit every 2 weeks -</p>
    <div class="package-price"><span class="price-figure">£2,500</span><span class="price-term">per<br>annum</span></div>
  </section>
  <section class="package" style="top:789px;">
    <div class="package-tab"><span>Package 2</span></div>
    <p class="package-note">Includes all the above + 1 Site Visit every week -</p>
    <div class="package-price"><span class="price-figure">£4,500</span><span class="price-term">per<br>annum</span></div>
  </section>
  <section class="package" style="top:959px;">
    <div class="package-tab"><span>Package 3</span></div>
    <p class="package-note">Includes all the above + 2 Site visits every week -</p>
    <div class="package-price"><span class="price-figure">£7,540</span><span class="price-term">per<br>annum</span></div>
  </section>

  <h3 class="net-heading" style="top:682px;">Internet Connectivity (medium/large Primary)</h3>
  <p class="net-item" style="left:59px; top:741px;">Managed Firewall</p>
  <p class="net-item" style="left:59px; top:773px; width:150px;">Managed Web filter &amp; Safe-guarding</p>
  <p class="net-item" style="left:59px; top:820px; width:160px;">User reporting portal/ email reporting.</p>
  <p class="net-item" style="left:59px; top:868px; width:170px;">Main Internet Line 1000 mb/s download 100mb/s upload</p>
  <p class="net-item" style="left:289px; top:756px; width:170px;">Back up Internet Line 80mb/s download 20mb/s upload</p>
  <p class="net-item" style="left:289px; top:806px;">100% uptime guaranteed.</p>
  <p class="net-item" style="left:289px; top:842px;">£3000 per annum</p>

  <h3 class="net-heading" style="top:931px;">Internet Connectivity (Small Primary School)</h3>
  <p class="net-item" style="left:64px; top:984px;">Managed Firewall</p>
  <p class="net-item" style="left:64px; top:1018px; width:140px; line-height:20px;">Managed Web filter &amp; Safeguarding</p>
  <p class="net-item" style="left:64px; top:1073px; width:160px; line-height:20px;">User reporting portal/email reporting.</p>
  <p class="net-item" style="left:289px; top:992px; width:170px; line-height:20px;">Main Internet Line 1000 mb/s download 100mb/s upload</p>
  <p class="net-item" style="left:289px; top:1040px;">£2100 per annum</p>

  <footer class="footer">
    <div class="footer-blue"></div>
    <div class="footer-phone">
      <svg width="24" height="24" viewBox="0 0 24 24" fill="none" stroke="#fff" stroke-width="1.6">
        <path d="M5 3 L9 3 L10.5 8 L8 10 C9.5 13 11 14.5 14 16 L16 13.5 L21 15 L21 19 C21 20 20 21 19 21 C10 20.5 3.5 14 3 5 C3 4 4 3 5 3 Z"/>
        <path d="M14 3 A7 7 0 0 1 21 10"/><path d="M14 6.5 A3.5 3.5 0 0 1 17.5 10"/>
      </svg>
      <span>0161 555 0142</span>
    </div>
    <div class="footer-link" style="left:322px;">
      <svg width="12" height="12" viewBox="0 0 12 12" fill="none" stroke="#fff" stroke-width="1">
        <circle cx="6" cy="6" r="5"/><ellipse cx="6" cy="6" rx="2.2" ry="5"/><line x1="1" y1="6" x2="11" y2="6"/>
      </svg>
      <span>varnoquell.co.uk</span>
    </div>
    <div class="footer-link" style="left:440px;">
      <svg width="13" height="10" viewBox="0 0 13 10" fill="none" stroke="#fff" stroke-width="1">
        <rect x="0.5" y="0.5" width="12" height="9"/><path d="M0.5 0.5 L6.5 5.5 L12.5 0.5"/>
      </svg>
      <span>info@varnoquell.co.uk</span>
    </div>
    <div class="footer-brand"><span class="brand-square"></span><span>VARNOQUELL</span></div>
  </footer>

</main>
</body>
</html>
```